The Best Real Estate Post Card Ever

Create a memorable and attention grabbing postcard BACK to be used the same every month and sent to 20,000 homes. The front of the postcard will change, I will make this every month. But the back I want to be known as ME and when people see it after years they instantly think of ME. This is all about branding and getting to be known as the agent to call when they need to move. I have attached styles I have used on past marketing. This design must work with both 11x8.5 and 9x6 and allow room for the postage to flow nicely.

Target Market(s)

Luxury waterfront clients

Colors
ec1f27
0255a3
ffffff

Requirements
Must have
• Clean and modern, luxury feel to it.
Nice to have
• Attention grabbing way to be remembered.
Should not have
• cheap look

```html
<!DOCTYPE html>
<html lang="en">
<head>
<meta charset="utf-8">
<title>Just Sold / Results That Move You – Postcard</title>
<link rel="stylesheet" href="https://fonts.googleapis.com/css2?family=Archivo+Black&family=Montserrat:wght@400;600;800&family=Cinzel:wght@500;700&family=Cormorant+Garamond:wght@700&display=swap">
<style>
:root{
  --navy:#1b2a5c;
  --red:#b01e32;
  --red-bright:#ec1f27;
  --white:#ffffff;
  --paper:#f3f3f4;
  --stage:#a9aaae;
  --ink:#1b2a5c;
}
*{margin:0;padding:0;box-sizing:border-box}
html,body{width:1200px;height:2589px;overflow:hidden;background:var(--stage)}
.card{position:absolute;left:122px;width:955px;height:740px;overflow:hidden;font-family:"Montserrat",sans-serif}
.card--front{top:520px;background:var(--navy)}
.card--back{top:1330px;background:var(--paper)}
.shapes{position:absolute;inset:0;width:955px;height:740px}
.photo{position:absolute;border:6px solid var(--white)}
.photo--main{left:30px;top:30px;width:405px;height:312px;background:linear-gradient(180deg,#9fc3dd 0%,#c8b892 45%,#5e7a3a 100%)}
.photo--pool{left:40px;top:338px;width:190px;height:135px;background:linear-gradient(160deg,#7b6a56,#5ec3d8)}
.photo--kitchen{left:236px;top:338px;width:190px;height:135px;background:linear-gradient(160deg,#e8e2d6,#c89a55 60%,#555)}
.person{position:absolute;background:linear-gradient(180deg,rgba(170,140,120,.85),rgba(90,95,105,.95));border-radius:120px 120px 0 0}
.person--front{left:620px;top:380px;width:300px;height:360px}
.person--back{left:360px;top:480px;width:210px;height:260px}
.headline{position:absolute;right:30px;font-family:"Archivo Black",sans-serif;color:var(--white);line-height:.82;text-align:right;letter-spacing:-4px}
.headline--just{top:28px;font-size:104px}
.headline--sold{top:112px;right:26px;font-size:140px;letter-spacing:-6px}
.offer{position:absolute;left:535px;display:flex;align-items:center;gap:12px;color:var(--white)}
.offer__big{font-family:"Archivo Black",sans-serif;font-size:60px;letter-spacing:-3px;line-height:1}
.offer__text{font-weight:600;font-size:18px;line-height:1.2;letter-spacing:-.5px}
.offer__text b{font-weight:800}
.offer--commission{top:262px}
.offer--credit{top:330px}
.offer-rule{position:absolute;left:535px;top:323px;width:390px;border-top:2px dashed rgba(255,255,255,.6)}
.badge-sold{position:absolute;left:362px;top:420px;width:126px;height:126px;border-radius:50%;background:var(--red);border:4px solid var(--white);color:var(--white);font-family:"Archivo Black",sans-serif;text-align:center;line-height:.95;padding-top:22px;letter-spacing:-1px}
.badge-sold span{display:block;font-size:24px}
.badge-sold small{display:block;font-size:19px}
.brand-seal{position:absolute;border-radius:50%;background:var(--white);border:6px solid var(--red);display:flex;align-items:center;justify-content:center;text-align:center}
.brand-seal__name{font-family:"Cinzel",serif;font-weight:700;color:var(--red);line-height:1.15}
.brand-seal--front{left:375px;top:520px;width:180px;height:180px}
.brand-seal--front .brand-seal__name{font-size:22px}
.brand-seal--back{left:318px;top:62px;width:170px;height:170px}
.brand-seal--back .brand-seal__name{font-size:20px}
.listing{position:absolute;left:40px;color:var(--white);font-weight:800}
.listing--address{top:505px;font-size:25px}
.listing--price{top:545px;font-size:32px}
.pin{display:inline-block;width:12px;height:12px;border-radius:50% 50% 50% 0;transform:rotate(-45deg);background:var(--red-bright);margin-right:8px;opacity:.7}
.contact{position:absolute;color:var(--white);font-size:24px;font-weight:600;line-height:1.45}
.contact--front{left:38px;top:655px}
.contact--back{left:26px;top:662px;font-size:20px}
.contact i{display:inline-block;width:13px;height:13px;background:var(--red-bright);border-radius:3px;margin-right:10px}
.agent-tag{position:absolute;right:0;top:660px;width:285px;height:68px;background:var(--red);color:var(--white);text-align:center;padding-top:4px}
.agent-name{font-family:"Cormorant Garamond",serif;font-weight:700;line-height:1}
.agent-tag .agent-name{font-size:40px}
.agent-creds{font-family:"Cinzel",serif;font-weight:500;letter-spacing:2px}
.agent-tag .agent-creds{font-size:17px}
.tagline{position:absolute;left:482px;top:228px;font-family:"Cinzel",serif;font-weight:500;color:var(--white);line-height:.98;font-size:56px}
.tagline span{font-size:72px}
.perks{position:absolute;left:26px;top:30px;list-style:none;color:var(--ink)}
.perks li{display:flex;align-items:flex-start;gap:16px;height:56px;font-size:17px;line-height:1.15}
.perks b{font-weight:800}
.perk-icon{width:32px;height:30px;flex:none;margin-top:2px}
.agent-block{position:absolute;left:26px;top:556px;color:var(--white)}
.agent-block .agent-name{font-size:50px}
.agent-block .agent-creds{font-size:24px;margin-top:4px}
.agent-rule{width:200px;height:5px;background:var(--red);margin-top:12px}
</style>
</head>
<body>

<section class="card card--front" aria-label="Postcard front">
  <svg class="shapes" viewBox="0 0 955 740" aria-hidden="true">
    <path d="M478 0H955V470C830 520 690 560 520 590 470 470 450 300 470 150 475 80 478 40 478 0Z" fill="var(--red)"/>
    <path d="M462 0C440 120 440 330 500 500" stroke="var(--white)" stroke-width="8" fill="none"/>
    <path d="M0 500H310L290 540H0Z" fill="var(--red)"/>
    <path d="M0 600C300 590 600 560 955 470V500C620 580 320 625 0 640Z" fill="var(--red)"/>
    <path d="M590 95C520 100 440 140 385 210" stroke="var(--white)" stroke-width="5" fill="none"/>
    <path d="M377 222l6-34 24 20z" fill="var(--white)"/>
  </svg>
  <div class="photo photo--main" role="img" aria-label="Photo of the sold home: single-storey house with garage, palm tree and lawn"></div>
  <div class="photo photo--pool" role="img" aria-label="Photo of the screened pool area"></div>
  <div class="photo photo--kitchen" role="img" aria-label="Photo of the kitchen with wood cabinets"></div>

  <div class="headline headline--just">JUST</div>
  <div class="headline headline--sold">SOLD</div>
  <div class="offer offer--commission"><span class="offer__big">1%</span><span class="offer__text">LIST YOUR HOME <small>FOR AS</small><br><small>LOW AS</small> <b>1% COMMISSION</b></span></div>
  <div class="offer-rule"></div>
  <div class="offer offer--credit"><span class="offer__big">10K</span><span class="offer__text">RECEIVE UP TO <b>$10,000</b> WHEN<br>YOU <b>BUY NEXT HOME</b> WITH ME</span></div>

  <div class="person person--front" role="img" aria-label="Portrait of the agent holding his young son"></div>

  <div class="badge-sold"><span>SOLD</span><small>IN ONLY</small><span>22 DAYS</span></div>

  <div class="listing listing--address"><span class="pin"></span>4820 BAYVIEW</div>
  <div class="listing listing--price">$310,000</div>

  <div class="brand-seal brand-seal--front"><span class="brand-seal__name">MARCO<br>VENTURI<br>HARBOR CREST</span></div>

  <div class="contact contact--front"><div><i></i>(555) 014-2286</div><div><i></i>MarcoVenturi@HarborCrest.net</div></div>

  <div class="agent-tag"><div class="agent-name">Marco Venturi,</div><div class="agent-creds">CRS, ABR, SRS, PSA</div></div>
</section>

<section class="card card--back" aria-label="Postcard back">
  <svg class="shapes" viewBox="0 0 955 740">
    <defs>
      <linearGradient id="sunset-home" x1="0" y1="0" x2="0" y2="1">
        <stop offset="0" stop-color="#5f6e9a"/>
        <stop offset=".22" stop-color="#d59a72"/>
        <stop offset=".5" stop-color="#6a6660"/>
        <stop offset="1" stop-color="#4f5a66"/>
      </linearGradient>
    </defs>
    <g role="img" aria-label="Photo of a luxury home with stone front, garage and paver driveway at sunset">
      <path d="M425 0H955V300C800 380 620 440 430 480C455 320 455 150 425 0Z" fill="url(#sunset-home)"/>
    </g>
    <path d="M430 480C460 340 520 260 600 225C720 260 850 240 955 195V300C800 380 620 440 430 480Z" fill="var(--navy)" opacity=".9"/>
    <path d="M318 0H400C440 150 445 320 430 480L416 482C428 320 420 150 380 0Z" fill="var(--red)"/>
    <path d="M0 495C250 502 600 460 955 290V322C600 490 250 528 0 526Z" fill="var(--red)"/>
    <path d="M0 526C250 528 450 508 575 486V740H0Z" fill="var(--navy)"/>
    <path d="M955 322C760 430 660 470 575 486V740H955Z" fill="var(--white)"/>
  </svg>

  <div class="tagline">RESULTS<br>THAT <span>MOVE</span><br><span>YOU</span></div>

  <ul class="perks">
    <li><svg class="perk-icon" viewBox="0 0 32 30"><path d="M16 2l4 9 10 1-7.5 7 2 10L16 24l-8.5 5 2-10L2 12l10-1z" fill="var(--red)"/></svg><span><b>200+</b> 5star online reviews</span></li>
    <li><svg class="perk-icon" viewBox="0 0 32 30"><path d="M16 1a10 10 0 0 1 10 10c0 8-10 18-10 18S6 19 6 11A10 10 0 0 1 16 1z" fill="var(--red)"/><circle cx="16" cy="11" r="4" fill="var(--paper)"/></svg><span>Palm Shore County resident<br><b>20+ years</b></span></li>
    <li><svg class="perk-icon" viewBox="0 0 32 30"><circle cx="16" cy="15" r="13" fill="none" stroke="var(--red)" stroke-width="3"/><path d="M10 15l4 4 8-8" stroke="var(--red)" stroke-width="3" fill="none"/></svg><span><b>Certified</b> Luxury home<br>marketing specialist</span></li>
    <li><svg class="perk-icon" viewBox="0 0 32 30"><rect x="3" y="5" width="22" height="20" rx="2" fill="none" stroke="var(--navy)" stroke-width="3"/><circle cx="24" cy="22" r="7" fill="var(--red)"/></svg><span><b>Available 7days a week</b><br>from 8am till midnight</span></li>
    <li><svg class="perk-icon" viewBox="0 0 32 30"><circle cx="16" cy="15" r="12" fill="none" stroke="var(--red)" stroke-width="3"/><path d="M16 7v16M12 11h7M12 19h7" stroke="var(--red)" stroke-width="3"/></svg><span><b>$20,000,000+</b> in pending/sold<br>sales so far in 2021</span></li>
    <li><svg class="perk-icon" viewBox="0 0 32 30"><rect x="3" y="5" width="26" height="20" rx="2" fill="none" stroke="var(--red)" stroke-width="3"/><path d="M6 22l7-8 5 5 4-3 5 6" stroke="var(--red)" stroke-width="2.5" fill="none"/></svg><span><b>Professional photography</b><br>included with every listing</span></li>
    <li><svg class="perk-icon" viewBox="0 0 32 30"><rect x="5" y="2" width="22" height="26" rx="2" fill="none" stroke="var(--red)" stroke-width="3"/><path d="M10 10h12M10 16h12M10 22h8" stroke="var(--red)" stroke-width="2.5"/></svg><span><b>Hassle free</b> listing agreements,<br>cancel anytime with no fees</span></li>
    <li><svg class="perk-icon" viewBox="0 0 32 30"><path d="M4 13h6v15H4zM12 13l6-10c3 0 3 3 2 7h8l-2 18H12z" fill="none" stroke="var(--red)" stroke-width="3" stroke-linejoin="round"/></svg><span><b>5star guarantee</b> - if i don't meet<br>your expectations, you don't pay me</span></li>
  </ul>

  <div class="brand-seal brand-seal--back"><span class="brand-seal__name">MARCO<br>VENTURI<br>HARBOR CREST</span></div>

  <div class="person person--back" role="img" aria-label="Portrait of the agent holding his young son"></div>

  <div class="agent-block">
    <div class="agent-name">Marco Venturi,</div>
    <div class="agent-creds">CRS, ABR, SRS, PSA</div>
    <div class="agent-rule"></div>
  </div>
  <div class="contact contact--back"><div><i></i>(555) 014-2286</div><div><i></i>MarcoVenturi@HarborCrest.net</div></div>
</section>

</body>
</html>
```